Christmas Collection Candle Label Design

Looking to update our existing Christmas Candle Collection labels. Labels should reflect the overall feel of our brand- www.kelvabrite.ca
Want to include some color elements. Holiday colors added into design but more muted/ earthy tones not vibrant colors . Metallic elements and line art botanical illustration. Fonts should be more align to brand
Scents
Winter Lantern
Frost Berry
Amber and Fig
Belle Étoile

```html
<!DOCTYPE html>
<html lang="en">
<head>
<meta charset="utf-8">
<title>Kelvabrite Christmas Collection Labels</title>
<link rel="stylesheet" href="https://fonts.googleapis.com/css2?family=Libre+Baskerville:wght@400;700&display=swap">
<style>
  :root {
    --bg-top: #afafaf;
    --bg-bottom: #d1bcab;
    --paper: #ffffff;
    --ink: #2b2320;
    --gold-light: #fbe7a6;
    --gold-mid: #f1cf75;
    --gold-deep: #d9a441;
    --sketch: #d4d4d4;

    --pine-band: #538a4c;
    --pine-title: #3e7a40;
    --pine-est: #9fcb9b;

    --frost-band: #5b90c1;
    --frost-title: #5b6e94;
    --frost-est: #9bb1cd;

    --amber-band: #bf785c;
    --amber-title: #7e4146;
    --amber-est: #d5a1a3;

    --etoile-band: #a92f39;
    --etoile-title: #7e4146;
    --etoile-est: #d5a1a3;
  }
  * { box-sizing: border-box; margin: 0; padding: 0; }
  html, body { width: 1173px; height: 1200px; overflow: hidden; }
  body {
    position: relative;
    background: linear-gradient(180deg, var(--bg-top), var(--bg-bottom));
    font-family: "Libre Baskerville", Georgia, serif;
  }
  .label {
    position: absolute;
    width: 490px;
    height: 490px;
    background: var(--paper);
    overflow: hidden;
    box-shadow: 0 14px 24px rgba(60, 40, 30, 0.25);
  }
  .label--pine { left: 76px; top: 72px; --band: var(--pine-band); --title: var(--pine-title); --est: var(--pine-est); }
  .label--frost { left: 603px; top: 72px; --band: var(--frost-band); --title: var(--frost-title); --est: var(--frost-est); }
  .label--amber { left: 76px; top: 611px; --band: var(--amber-band); --title: var(--amber-title); --est: var(--amber-est); }
  .label--etoile { left: 606px; top: 609px; --band: var(--etoile-band); --title: var(--etoile-title); --est: var(--etoile-est); }

  .color-band {
    position: absolute;
    left: 374px; top: 0;
    width: 116px; height: 100%;
    background: var(--band);
  }
  .botanical-art {
    position: absolute;
    background: radial-gradient(ellipse at center, rgba(200,200,200,0.55), rgba(200,200,200,0) 70%);
    mix-blend-mode: multiply;
  }
  .label--pine .botanical-art { left: 220px; top: 160px; width: 270px; height: 330px; }
  .label--frost .botanical-art { left: 230px; top: 100px; width: 260px; height: 320px; }
  .label--amber .botanical-art { left: 140px; top: 200px; width: 350px; height: 240px; }
  .label--etoile .botanical-art { left: 190px; top: 180px; width: 300px; height: 260px; }

  .gold-frame {
    position: absolute;
    left: 25px; top: 25px; right: 25px; bottom: 27px;
    border: 4px solid transparent;
    border-image: linear-gradient(135deg, var(--gold-light), var(--gold-deep) 35%, var(--gold-light) 60%, var(--gold-deep)) 1;
  }
  .brand {
    position: absolute;
    left: 58px; top: 62px;
    font-size: 14px;
    letter-spacing: 1px;
    color: var(--ink);
    display: flex; align-items: center; gap: 6px;
  }
  .brand-dot { width: 6px; height: 6px; border-radius: 50%; background: var(--ink); }
  .scent-title {
    position: absolute;
    left: 50px; top: 112px;
    font-weight: 700;
    font-size: 58px;
    line-height: 58px;
    color: var(--title);
    text-transform: uppercase;
    letter-spacing: 1px;
  }
  .scent-title small { font-size: 30px; letter-spacing: 1px; }
  .established {
    position: absolute;
    left: 52px; top: 246px;
    font-size: 27px;
    letter-spacing: 3px;
    color: var(--est);
  }
  .info-row {
    position: absolute;
    left: 33px; top: 408px;
    width: 424px; height: 48px;
    display: flex; gap: 5px;
  }
  .info-tag {
    flex: 1;
    display: flex; align-items: center; justify-content: center;
    text-align: center;
    font-size: 13px;
    line-height: 13px;
    color: var(--ink);
    background: linear-gradient(100deg, var(--gold-mid), var(--gold-light) 70%, rgba(251,231,166,0.85));
  }
</style>
</head>
<body>

  <section class="label label--pine">
    <div class="color-band"></div>
    <div class="botanical-art" role="img" aria-label="Line art of evergreen fir sprigs"></div>
    <div class="gold-frame"></div>
    <div class="brand"><span class="brand-dot"></span>KELVABRITE</div>
    <h2 class="scent-title">Winter<br>Lantern</h2>
    <p class="established">EST 2005</p>
    <div class="info-row">
      <div class="info-tag">Marketplace<br>connection</div>
      <div class="info-tag">Made with pure<br>essential oil</div>
      <div class="info-tag">Net weight: 120g</div>
    </div>
  </section>

  <section class="label label--frost">
    <div class="color-band"></div>
    <div class="botanical-art" role="img" aria-label="Line art of snowflakes"></div>
    <div class="gold-frame"></div>
    <div class="brand"><span class="brand-dot"></span>KELVABRITE</div>
    <h2 class="scent-title">Frost<br>Berry</h2>
    <p class="established">EST 2005</p>
    <div class="info-row">
      <div class="info-tag">Marketplace<br>connection</div>
      <div class="info-tag">Made with pure<br>essential oil</div>
      <div class="info-tag">Net weight: 120g</div>
    </div>
  </section>

  <section class="label label--amber">
    <div class="color-band"></div>
    <div class="botanical-art" role="img" aria-label="Line art of cinnamon sticks and cloves"></div>
    <div class="gold-frame"></div>
    <div class="brand"><span class="brand-dot"></span>KELVABRITE</div>
    <h2 class="scent-title">Amber <small>and</small><br>Fig</h2>
    <p class="established">EST 2005</p>
    <div class="info-row">
      <div class="info-tag">Marketplace<br>connection</div>
      <div class="info-tag">Made with pure<br>essential oil</div>
      <div class="info-tag">Net weight: 120g</div>
    </div>
  </section>

  <section class="label label--etoile">
    <div class="color-band"></div>
    <div class="botanical-art" role="img" aria-label="Line art of star anise and cloves"></div>
    <div class="gold-frame"></div>
    <div class="brand"><span class="brand-dot"></span>KELVABRITE</div>
    <h2 class="scent-title">Belle<br>Étoile</h2>
    <p class="established">EST 2005</p>
    <div class="info-row">
      <div class="info-tag">Marketplace<br>connection</div>
      <div class="info-tag">Made with pure<br>essential oil</div>
      <div class="info-tag">Net weight: 120g</div>
    </div>
  </section>

</body>
</html>
```